Telmora Coaching flyer (women local)

Strapline: Do you want a more fulfilling and meaningful life?
Make 2015 a year for positive change

Image of an attractive woman in contemplation:

• I’ve lost my identity and wondering what life is about.

• I want more intimacy in my relationship

• I hate my career and don’t know what’s right for me

Personal Development Coaching can help you:

Testimonials from our clients:

‘I have changed the way I approach my daily life in order to achieve more for myself’.

‘Coaching has helped me change the way I think, focusing more on positive rather than negative thoughts’.

‘Without coaching, I believe that my life would have remained stagnant’.

‘ I have made the leap to set up my own business and have increased my income three fold’.

‘Coaching has helped me to grow closer than ever to my husband’.

Any relevant image and image of myself (included)

Why Telmora?

• Certified Personal Development Coach

• Experience coaching individuals wanting to effect change

Nadia is a specialist in coaching for:

• Building confidence

• Feeling motivated and getting out of a rut

• Enhancing relationships with partners or family

• Making changes in your career or business

Book your free consultation (this should stand out)

e: nadia@telmora-example.co.uk t: 0798 512 6043 w: www.telmora-example.co.uk (include logo, but change ‘Telmora Consulting’ to ‘Telmora Coaching’)
f: www.facebook.com/telmora-example.co.uk t: @ndtelmora

* Notes in brackets are only instructions and not to be included as part of the flyer.

Flyer is is A5

Please not this flyer can be double sided as I feel there will be too much text for one side. Could you use image of woman in contemplation on front but not too depressing.

```html
<!DOCTYPE html>
<html lang="en">
<head>
<meta charset="utf-8">
<title>Telmora Coaching – Flyer</title>
<link rel="stylesheet" href="https://fonts.googleapis.com/css2?family=Roboto+Condensed:wght@400;700&display=swap">
<style>
  :root {
    --navy: #143a72;
    --ink: #1a1a1a;
    --sky: #a8dbf2;
    --paper: #ffffff;
    --mist: #dcdcdc;
    --sand-light: #f4ece3;
    --sand: #e2d3c2;
    --band: #0e2f66;
    --rule: #3fb3e3;
    --photo-warm: #7a3f25;
    --photo-dark: #24242c;
  }
  html, body { margin: 0; padding: 0; overflow: hidden; background: #ffffff; }
  .flyer {
    position: relative; width: 927px; height: 1200px; overflow: hidden;
    font-family: "Roboto Condensed", "Arial Narrow", sans-serif;
    color: var(--navy);
    background: var(--paper);
  }
  .abs { position: absolute; margin: 0; }

  .top-panel {
    left: 0; top: 0; width: 927px; height: 443px;
    background: linear-gradient(180deg, #ffffff 0%, #f3f3f3 55%, var(--mist) 100%);
  }
  .middle-panel {
    left: 0; top: 443px; width: 927px; height: 450px;
    background: linear-gradient(100deg, var(--sand) 0%, var(--sand-light) 45%, #efe6dc 100%);
  }
  .middle-panel::before {
    content: ""; position: absolute; left: 0; top: 0; width: 100%; height: 28px;
    background: linear-gradient(180deg, rgba(0,0,0,0.28), rgba(0,0,0,0));
  }
  .bottom-panel {
    left: 0; top: 893px; width: 927px; height: 307px;
    background: linear-gradient(180deg, #ffffff 0%, #f1f1f1 60%, #e2e2e2 100%);
  }
  .diagonals { left: 0; top: 0; width: 927px; height: 1200px; pointer-events: none; }

  .why-title { left: 44px; top: 58px; font-size: 31px; line-height: 38px; font-weight: 700; }
  .why-list { left: 44px; top: 112px; list-style: none; padding: 0; font-size: 25px; line-height: 31px; }
  .why-list li { position: relative; padding-left: 25px; margin-bottom: 15px; }
  .why-list li::before { content: "•"; position: absolute; left: 0; }

  .testimonials-title { left: 484px; top: 62px; font-size: 21px; line-height: 26px; font-weight: 700; color: var(--ink); }
  .quote { font-size: 21px; line-height: 27px; color: var(--ink); white-space: nowrap; }

  .photo {
    left: 88px; top: 460px; width: 298px; height: 433px;
    background: radial-gradient(ellipse at 45% 35%, var(--photo-warm) 0%, #5e3020 40%, #2b2b33 75%, var(--photo-dark) 100%);
  }

  .specialist-title { left: 402px; top: 505px; font-size: 24.5px; line-height: 30px; font-weight: 700; }
  .specialist-list { left: 402px; top: 546px; list-style: none; padding: 0; font-size: 26.5px; line-height: 33px; }
  .specialist-list li { position: relative; padding-left: 26px; margin-bottom: 9px; }
  .specialist-list li::before { content: "•"; position: absolute; left: 2px; }

  .cta { left: 505px; top: 833px; font-size: 32.5px; line-height: 40px; font-weight: 700; }

  .brand-dot { left: 199px; top: 940px; width: 36px; height: 36px; border-radius: 50%; background: var(--navy); }
  .brand { left: 92px; top: 1060px; width: 250px; text-align: center; font-size: 40px; line-height: 46px; letter-spacing: 1px; color: var(--navy); }

  .contact { left: 524px; top: 934px; list-style: none; padding: 0; font-size: 21px; line-height: 28px; white-space: nowrap; }
  .contact li { margin-bottom: 14.5px; }

  .rule { left: 0; top: 1160px; width: 927px; height: 3px; background: var(--rule); }
  .footer-band { left: 0; top: 1168px; width: 927px; height: 32px; background: var(--band); }
</style>
</head>
<body>
<main class="flyer">
  <div class="abs top-panel"></div>
  <div class="abs middle-panel"></div>
  <div class="abs bottom-panel"></div>

  <svg class="abs diagonals" viewBox="0 0 927 1200" aria-hidden="true">
    <defs>
      <linearGradient id="skyFade" x1="0" y1="0" x2="1" y2="1">
        <stop offset="0" stop-color="#9fd7f1"/>
        <stop offset="1" stop-color="#c6ebfa"/>
      </linearGradient>
      <linearGradient id="ctaFade" x1="0" y1="0" x2="1" y2="0">
        <stop offset="0" stop-color="#bfe7f8"/>
        <stop offset="1" stop-color="#93d1ee"/>
      </linearGradient>
    </defs>
    <polygon points="0,0 500,0 0,550" fill="url(#skyFade)"/>
    <polygon points="0,443 97,443 0,550" fill="#8fcfee"/>
    <polygon points="425,808 927,808 927,893 505,893" fill="url(#ctaFade)"/>
  </svg>

  <h2 class="abs why-title">Why Telmora?</h2>
  <ul class="abs why-list">
    <li>Certified Personal<br>Development Coach</li>
    <li>Experience coaching<br>individuals wanting<br>to effect change</li>
  </ul>

  <h3 class="abs testimonials-title">Testimonials from our clients:</h3>
  <p class="abs quote" style="left:449px; top:100px;">&nbsp;‘I have changed the way I approach my daily life<br>in order to achieve more for myself’.</p>
  <p class="abs quote" style="left:388px; top:169px;">‘Coaching has helped me change the way I think,<br>&nbsp;focusing more on positive rather than negative thoughts’.</p>
  <p class="abs quote" style="left:330px; top:236px;">‘Without coaching, I believe that my life would have<br>&nbsp;remained stagnant’.</p>
  <p class="abs quote" style="left:267px; top:304px;">‘ I have made the leap to set up my own business and have increased<br>&nbsp;my income three fold’.</p>
  <p class="abs quote" style="left:205px; top:373px;">‘Coaching has helped me to grow closer than ever to my husband’.</p>

  <div class="abs photo" role="img" aria-label="Portrait photograph of Nadia, the coach, smiling with arms folded"></div>

  <h3 class="abs specialist-title">Nadia is a specialist in coaching for:</h3>
  <ul class="abs specialist-list">
    <li>Building confidence</li>
    <li>Feeling motivated and getting out of a rut</li>
    <li>Enhancing relationships with<br>partners or family</li>
    <li>Making changes in your career or business</li>
  </ul>

  <p class="abs cta">Book your free consultation</p>

  <span class="abs brand-dot" aria-hidden="true"></span>
  <p class="abs brand">TELMORA<br>COACHING</p>

  <ul class="abs contact">
    <li>e: nadia@telmora-example.co.uk</li>
    <li>t: 0798 512 6043</li>
    <li>w: www.telmora-example.co.uk</li>
    <li>f: www.facebook.com/telmora-example.co.uk</li>
    <li>t: @ndtelmora</li>
  </ul>

  <div class="abs rule"></div>
  <div class="abs footer-band"></div>
</main>
</body>
</html>
```